Bref créative
Brightwater Realty and Acreage
12%-20% guaranteed returns by law
I need double sided standard sized Business Card [3.5" x 2"]
Open to different fonts
Professional
Marcus Holt
C.E.O
Tampa Florida,
info@brightwaterrealtyandacreage.com
Color of card should be blue. Lettering orange. Please check our website. The website is still under construction but it will give you ideas and colors etc. The logo was designed by Vexly!
Incorporate logo. 12%- 20% guaranteed returns by law. Worldwide opportunity. Offices in Washington DC, Tampa Florida, Oxford England, Melbourne Australia

```html
<!DOCTYPE html>
<html lang="en">
<head>
<meta charset="utf-8">
<title>Brightwater Realty and Acreage – Business Cards</title>
<link href="https://fonts.googleapis.com/css2?family=Open+Sans:wght@400;600;700;800&display=swap" rel="stylesheet">
<style>
  :root {
    --page-bg: #5b5b5e;
    --blue-deep: #0a2a8c;
    --blue-bright: #2a6cf0;
    --black: #050505;
    --orange: #ff8a00;
    --orange-light: #ffb21e;
    --white: #ffffff;
  }
  * { margin: 0; padding: 0; box-sizing: border-box; }
  html, body { width: 1200px; height: 852px; overflow: hidden; }
  body {
    background: var(--page-bg);
    font-family: "Open Sans", Arial, sans-serif;
    position: relative;
  }
  .card {
    position: absolute;
    width: 540px;
    height: 309px;
    border-radius: 16px;
    overflow: hidden;
    box-shadow: 0 8px 22px rgba(0,0,0,0.45);
  }
  .card-shape { position: absolute; inset: 0; }
  .card-front { left: 70px; top: 110px; }
  .card-back { left: 590px; top: 430px; }

  .holder { position: absolute; left: 22px; top: 34px; color: var(--white); }
  .holder-name { font-size: 17px; font-weight: 700; }
  .holder-title { font-size: 10px; font-weight: 400; margin-top: 2px; }

  .contact-list {
    position: absolute; left: 22px; top: 150px;
    list-style: none; color: var(--white); font-size: 10.5px; line-height: 18px;
  }
  .contact-list li { display: flex; align-items: center; gap: 7px; }
  .contact-list svg { width: 11px; height: 11px; flex: none; }

  .brand-lockup {
    position: absolute; left: 352px; top: 36px; width: 172px;
    display: flex; flex-direction: column; align-items: center; gap: 8px;
  }
  .brand-mark { width: 60px; height: 60px; border-radius: 50%; background: var(--orange); }
  .brand-name {
    color: var(--orange); font-weight: 700; font-size: 12px;
    text-align: center; letter-spacing: 0.4px; text-transform: uppercase; line-height: 1.3;
  }

  .back-brand {
    position: absolute; left: 40px; top: 100px; width: 190px;
    display: flex; flex-direction: column; align-items: center; gap: 12px;
  }
  .back-brand .brand-mark { width: 78px; height: 78px; }
  .back-brand .brand-name { font-size: 13px; }

  .offer { position: absolute; right: 22px; top: 58px; width: 230px; text-align: right; color: var(--white); }
  .offer-kicker { font-size: 11px; font-weight: 700; }
  .offer-rate { font-size: 40px; font-weight: 800; color: var(--orange); line-height: 1; margin-top: 30px; letter-spacing: -0.5px; }
  .offer-note { font-size: 14px; font-weight: 700; margin-top: 4px; }
  .offices { font-size: 9.5px; line-height: 15px; margin-top: 34px; }
</style>
</head>
<body>

<section class="card card-front" aria-label="Business card front">
  <svg class="card-shape" viewBox="0 0 540 309" aria-hidden="true">
    <defs>
      <linearGradient id="blueFront" x1="0" y1="0" x2="1" y2="1">
        <stop offset="0" stop-color="#1f58e0"/>
        <stop offset="0.6" stop-color="#0d35b0"/>
        <stop offset="1" stop-color="#071f78"/>
      </linearGradient>
    </defs>
    <rect width="540" height="309" fill="url(#blueFront)"/>
    <path d="M200,0 C290,70 320,220 540,262 L540,0 Z" fill="var(--orange)"/>
    <path d="M214,0 C300,72 334,208 540,248 L540,0 Z" fill="var(--black)"/>
  </svg>
  <div class="holder">
    <p class="holder-name">Marcus Holt</p>
    <p class="holder-title">C.E.O</p>
  </div>
  <ul class="contact-list">
    <li><svg viewBox="0 0 12 12"><path d="M6 1 L11 6 H9.5 V11 H7 V8 H5 V11 H2.5 V6 H1 Z" fill="#fff"/></svg>Tampa Florida,</li>
    <li><svg viewBox="0 0 12 12"><path d="M3 1 L5 3.5 L4 5 C5 7 6 8 7 8 L8.5 7 L11 9 L9.5 11 C5 11 1 7 1 2.5 Z" fill="#fff"/></svg>(1) 1-877-555-0142</li>
    <li><svg viewBox="0 0 12 12"><rect x="3" y="0.5" width="6" height="11" rx="1.2" fill="#fff"/></svg>813-555-0187</li>
    <li><svg viewBox="0 0 12 12"><circle cx="6" cy="6" r="5.5" fill="#fff"/><rect x="3" y="4" width="6" height="4" fill="var(--blue-deep)"/></svg>info@brightwaterrealtyandacreage.com</li>
    <li><svg viewBox="0 0 12 12"><circle cx="6" cy="6" r="5" fill="none" stroke="#fff" stroke-width="1.2"/><path d="M1 6 H11 M6 1 C3 4 3 8 6 11 C9 8 9 4 6 1" fill="none" stroke="#fff" stroke-width="0.9"/></svg>www.brightwaterrealtyandacreage.com</li>
  </ul>
  <div class="brand-lockup">
    <span class="brand-mark" aria-hidden="true"></span>
    <p class="brand-name">Brightwater Realty<br>and Acreage</p>
  </div>
</section>

<section class="card card-back" aria-label="Business card back">
  <svg class="card-shape" viewBox="0 0 540 309" aria-hidden="true">
    <defs>
      <linearGradient id="blueBack" x1="0" y1="0" x2="1" y2="1">
        <stop offset="0" stop-color="#2a6cf0"/>
        <stop offset="0.5" stop-color="#1243c8"/>
        <stop offset="1" stop-color="#081f7a"/>
      </linearGradient>
    </defs>
    <rect width="540" height="309" fill="url(#blueBack)"/>
    <path d="M0,0 L340,0 C318,110 300,220 262,309 L0,309 Z" fill="var(--orange)"/>
    <path d="M0,0 L326,0 C304,110 286,220 248,309 L0,309 Z" fill="var(--black)"/>
  </svg>
  <div class="back-brand">
    <span class="brand-mark" aria-hidden="true"></span>
    <p class="brand-name">Brightwater</p>
  </div>
  <div class="offer">
    <p class="offer-kicker">Worldwide investment opportunity</p>
    <p class="offer-rate">12%- 20%</p>
    <p class="offer-note">guaranteed returns by law.</p>
    <p class="offices">Washington DC / Tampa Florida<br>/ Oxford England / Melbourne Australia</p>
  </div>
</section>

</body>
</html>
```